New webpage for Facility Management Company (cleaning services)

We need a new web page design for a company based in Stockholm, Sweden, called TRV Clean AB (established 1991). We provide cleaning services to the public sector, to businesses, and to home owners. Our services primarily include daily cleaning, floor care, window cleaning, and carpet cleaning.

Our company holds certificates for ISO 9001, ISO 14001, ISO 45001 and "Gnistan".

Referring to "the Swedish model" we honor collective agreements between Verosa (employer-representative organisation and relevant labour unions (e.g. Bärkraft).
The final design should communicate that we are a trustworthy company with a well trained staff, high quality services combined with a commitment to run a sustainable business from a labour and environmental perspective.

DETAILS
General
-----------------------------------------------
• Language: Swedish (we provide text)
• Very important: Easy to administrate for company staff without special technical skills, especially to
o add/change information about HQ staff
o change any text
o add/change information about offered services
• Responsive
• SEO-friendly

Content that web page needs to cover in one way or the other
--------------------------------------------
• Information about our company
• About our staff and contact info to HQstaff/management (photos, contact info)
• Our ambitions and supporting info (quality, environment, labour conditions, certificates, etc)
• Information to customers within the public sector
• Information to customers within the private sector
• Information to customers within the home owner sector
• Services public sector (Swedish = Offentlig sektor)
• Services private business sector (Swedish = Företag) Se berglöf
• Services home owner sector (Swedish=Privat)
• GDPR compliance
• News

Content/Function
-------------------------------
• One specific requirement is that we need a page for information to potentially new employees (some general information and open job positions) with a possibility to fill in a simple application form and upload CV.(Mail?) CAPTCHA or equivalent.
• Contact form for customers with CAPTCHA or equivalent.
• Cookie management
• Integration social media (future); easy to manage/add/delete integration of social media.

We are not interested in a blog at this point of time

```html
<!DOCTYPE html>
<html lang="en">
<head>
<meta charset="utf-8">
<title>TRV Clean AB – Cleaning Services</title>
<link href="https://fonts.googleapis.com/css2?family=Libre+Baskerville:wght@400;700&family=Poppins:wght@400;500;600;700&display=swap" rel="stylesheet">
<style>
:root{
  --green:#4cb848;
  --green-dark:#3fa63c;
  --blue:#1a8ee0;
  --blue-dark:#1479c4;
  --purple:#9b5fb8;
  --yellow:#f2b71c;
  --ink:#1d1d1f;
  --text:#666a70;
  --night:#15171f;
  --line:#e4e6ea;
  --white:#ffffff;
  --serif:"Libre Baskerville", Georgia, serif;
  --sans:"Poppins", Arial, sans-serif;
}
*{box-sizing:border-box;margin:0;padding:0}
html,body{width:1200px;height:4319px;overflow:hidden}
body{font-family:var(--sans);color:var(--ink);background:var(--white)}
.page{position:relative;width:1200px;height:4319px;overflow:hidden}
.abs{position:absolute}
a{color:inherit;text-decoration:none}
.serif{font-family:var(--serif)}

/* top bar */
.topbar{position:absolute;left:0;top:0;width:1200px;height:34px;background:var(--blue);color:var(--white);font-size:11px;font-weight:500}
.topbar .item{position:absolute;top:0;height:34px;display:flex;align-items:center;gap:7px}
.topbar .divider{position:absolute;left:402px;top:6px;width:1px;height:22px;background:rgba(255,255,255,.35)}
.topbar .apply{position:absolute;left:907px;top:0;width:199px;height:34px;background:var(--blue-dark);display:flex;align-items:center;justify-content:center;font-size:11px;font-weight:600;letter-spacing:.2px}

/* header */
.logo{display:flex;align-items:center;gap:8px;font-family:var(--serif);font-weight:400;color:var(--ink)}
.logo .dot{width:22px;height:22px;border-radius:50%;background:var(--green)}
.site-logo{left:84px;top:72px;font-size:30px}
.nav{position:absolute;left:419px;top:88px;display:flex;gap:30px;font-size:11.5px;font-weight:500;color:var(--ink);text-transform:uppercase}
.nav .active{color:var(--green);position:relative}
.nav .active::after{content:"";position:absolute;left:0;right:0;bottom:-9px;height:2px;background:var(--green)}

/* hero */
.hero-title{left:84px;top:258px;font-family:var(--serif);font-weight:700;font-size:57px;line-height:72px;letter-spacing:-.5px;color:var(--ink)}
.hero-text{left:84px;top:420px;width:430px;font-size:14.5px;line-height:25px;color:var(--text)}
.btn{display:flex;align-items:center;justify-content:center;border-radius:30px;background:var(--green);color:var(--white);font-weight:600;text-transform:uppercase}
.hero-btn{left:85px;top:496px;width:277px;height:54px;font-size:13px}
.hero-art{left:600px;top:140px;width:560px;height:480px}
.card{background:var(--white);border-radius:10px;box-shadow:0 8px 26px rgba(20,30,60,.12)}
.person-card{left:531px;top:546px;width:160px;height:62px;display:flex;align-items:center;gap:10px;padding:0 14px}
.avatar{width:34px;height:34px;border-radius:8px;background:linear-gradient(135deg,#f4a7b0,#3aa1d8)}
.person-card b{display:block;font-size:11px;font-weight:500;color:#333}
.person-card span{display:block;font-size:8.5px;color:var(--blue)}
.staff-card{left:838px;top:580px;width:129px;height:110px;padding:12px 14px}
.staff-card .label{font-size:10px;color:#333}
.faces{display:flex;margin:10px 0 8px}
.faces i{width:27px;height:27px;border-radius:50%;border:2px solid #fff;margin-right:-8px;display:block}
.faces i.count{background:#3b1e3a;color:#fff;font-size:8px;font-style:normal;display:flex;align-items:center;justify-content:center}
.rating{font-size:9px;color:#333;display:flex;align-items:center;gap:4px}
.rating small{font-size:7px;color:#999}
.slider-dots{left:573px;top:702px;display:flex;gap:9px}
.slider-dots i{width:9px;height:9px;border-radius:50%;background:#d7d9dd;display:block}
.slider-dots i.on{background:var(--ink)}

/* certificates */
.cert-line{left:0;top:776px;width:1200px;text-align:center;font-family:var(--serif);font-weight:700;font-size:20px;line-height:36px;color:var(--ink);text-decoration:underline;text-underline-offset:5px}

/* about */
.about-img{left:0;top:900px;width:548px;height:530px}
.eyebrow{left:615px;top:1010px;font-size:16px;font-weight:600;color:#9aa0a6}
.about-title{left:615px;top:1038px;font-family:var(--serif);font-weight:700;font-size:38px;color:var(--ink)}
.about-rule{left:615px;top:1093px;width:52px;height:2px;background:#d9dbe0}
.about-text{left:615px;top:1110px;width:465px;font-size:13.5px;line-height:23.2px;color:var(--text)}
.about-btn{left:615px;top:1304px;width:155px;height:41px;font-size:11.5px}

/* section titles */
.section-title{left:0;width:1200px;text-align:center;font-family:var(--serif);font-weight:700;font-size:37px;color:var(--ink)}
.title-rule{width:62px;height:2px;background:#d9dbe0}

/* ambitions */
.ambitions{left:0;top:1569px;width:1200px;height:180px}
.ambition{position:absolute;top:0;width:200px;margin-left:-100px;text-align:center}
.ambition .circle{width:120px;height:120px;border-radius:50%;margin:0 auto;display:flex;align-items:center;justify-content:center;box-shadow:inset -14px -14px 0 rgba(0,0,0,.12)}
.ambition p{margin-top:22px;font-family:var(--serif);font-weight:700;font-size:16px;color:var(--ink)}
.dots3{position:absolute;top:54px;display:flex;gap:6px;align-items:center}
.dots3 i{width:6px;height:6px;border-radius:50%;background:#cfd3d8;display:block}

/* services */
.services-bg{left:0;top:1770px;width:1200px;height:510px}
.products-img{left:838px;top:1780px;width:235px;height:215px;border-radius:10px}
.services-title{top:1995px;color:var(--white)}
.service{position:absolute;top:2095px;width:245px;height:340px;background:var(--white);border-radius:4px;box-shadow:0 8px 26px rgba(20,30,60,.1);text-align:center;overflow:hidden}
.service .photo{height:183px}
.service h3{margin-top:28px;font-family:var(--serif);font-weight:700;font-size:16px;color:var(--ink)}
.service p{margin:18px auto 0;width:200px;font-size:12.5px;line-height:20px;color:var(--text)}

/* customers */
.customers-title{left:137px;top:2530px;font-family:var(--serif);font-weight:700;font-size:37px;color:var(--ink)}
.customers-rule{left:139px;top:2591px;width:60px;height:2px;background:#d9dbe0}
.customer{position:absolute;width:270px}
.customer svg{display:block}
.customer h4{margin-top:14px;font-family:var(--serif);font-weight:700;font-size:15px;color:var(--ink)}
.customer p{margin-top:10px;font-size:12px;line-height:20px;color:var(--text)}
.worker-art{left:740px;top:2480px;width:330px;height:520px}

/* news */
.news-title{top:3025px}
.news{position:absolute;top:3122px;width:280px;height:396px;background:var(--white);border-radius:6px;box-shadow:0 8px 26px rgba(20,30,60,.1);overflow:hidden}
.news .photo{height:210px}
.news .body{padding:22px 20px 0}
.news time{font-size:11.5px;color:#8a8f96;display:block}
.news h3{margin-top:10px;font-family:var(--serif);font-weight:700;font-size:15.5px;color:var(--ink)}
.news p{margin-top:14px;font-size:14px;line-height:22px;color:var(--text)}

/* footer */
.footer-bg{left:0;top:3690px;width:1200px;height:629px}
.cta{left:139px;top:3608px;width:924px;height:205px;border-radius:103px;background:var(--green)}
.cta .small{position:absolute;left:78px;top:62px;font-family:var(--serif);font-size:28px;color:var(--white)}
.cta .big{position:absolute;left:76px;top:102px;font-family:var(--serif);font-weight:700;font-size:54px;color:var(--white)}
.cta .go{position:absolute;left:676px;top:79px;width:184px;height:46px;border-radius:26px;background:var(--white);color:var(--ink);font-size:11.5px;font-weight:600;display:flex;align-items:center;justify-content:center;text-transform:uppercase}
.footer-logo{left:84px;top:4058px;font-size:34px;color:var(--white)}
.socials{left:157px;top:4116px;display:flex;gap:10px}
.socials i{width:44px;height:44px;border-radius:50%;background:#262932;display:block}
.footer h5{font-family:var(--serif);font-weight:700;font-size:17px;color:var(--white)}
.quick{left:427px;top:3974px}
.quick ul{list-style:none;margin-top:22px}
.quick li{font-size:12px;color:#d5d7dc;height:26.8px}
.contact{left:605px;top:3974px;width:210px}
.contact .row{display:flex;gap:10px;margin-top:18px;font-size:12px;line-height:17px;color:#d5d7dc}
.contact .row b{display:block;font-weight:600;color:var(--white);font-size:11.5px}
.newsletter{left:846px;top:3974px;width:260px}
.newsletter p{margin-top:16px;font-size:12px;line-height:18px;color:#d5d7dc}
.subscribe{margin-top:18px;height:46px;border-radius:24px;background:var(--white);display:flex;align-items:center;padding:0 16px;gap:8px;font-size:12px;color:#7b8088}
.subscribe span{flex:1}
.footer-rule{left:84px;top:4252px;width:1032px;height:1px;background:#2c2f38}
.copyright{left:0;top:4274px;width:1200px;text-align:center;font-size:12px;color:#d5d7dc}
.legal{left:915px;top:4274px;font-size:12px;color:#d5d7dc}
.to-top{left:1125px;top:4231px;width:42px;height:42px;border-radius:50%;background:var(--green);display:flex;align-items:center;justify-content:center}
</style>
</head>
<body>
<div class="page">

  <!-- top bar -->
  <div class="topbar">
    <div class="item" style="left:84px">
      <svg width="12" height="12" viewBox="0 0 12 12"><circle cx="6" cy="6" r="5.2" fill="none" stroke="#fff" stroke-width="1.5"/><path d="M6 3v3l2 1.3" fill="none" stroke="#fff" stroke-width="1.3"/></svg>
      Mon – Fri: 10AM – 7PM; Sat – Sun: 10AM – 3PM
    </div>
    <div class="divider"></div>
    <div class="item" style="left:437px">
      <svg width="12" height="12" viewBox="0 0 12 12"><path d="M2.5 1h2l1 3-1.3 1a7 7 0 0 0 2.8 2.8l1-1.3 3 1v2a1 1 0 0 1-1 1A9.5 9.5 0 0 1 1.5 2a1 1 0 0 1 1-1z" fill="#fff"/></svg>
      Call Us: (08) 555-0142
    </div>
    <div class="item" style="left:833px;font-size:10px">Eng
      <svg width="8" height="6" viewBox="0 0 8 6"><path d="M1 1l3 3 3-3" fill="none" stroke="#fff" stroke-width="1.3"/></svg>
    </div>
    <a class="apply" href="#">EMPLOYMENT APPLICATION</a>
  </div>

  <!-- header -->
  <a class="abs logo site-logo" href="#"><span class="dot"></span>TRV Clean AB</a>
  <nav class="nav">
    <a class="active" href="#">Home</a>
    <a href="#">About Us</a>
    <a href="#">Our Ambitions</a>
    <a href="#">Our Services</a>
    <a href="#">GDPR Compliance</a>
    <a href="#">News</a>
    <a href="#">Contact Us</a>
  </nav>

  <!-- hero -->
  <h1 class="abs hero-title">We Provide<br>Cleaning Services</h1>
  <p class="abs hero-text">For a company based in Stockholm, Sweden, called TRV Clean AB (established 1991).</p>
  <a class="abs btn hero-btn" href="#">Need Emergency Services ?</a>

  <svg class="abs hero-art" viewBox="0 0 560 480" role="img" aria-label="Smiling cleaner in blue apron holding a bucket of cleaning supplies in front of a green leaf shape">
    <path d="M160 10 C260 60 420 120 440 280 C455 400 360 470 250 470 C130 470 60 380 80 270 C95 180 130 90 160 10Z" fill="var(--green)"/>
    <rect x="150" y="40" width="260" height="430" rx="120" fill="#5fa8dc" opacity=".55"/>
  </svg>
  <svg class="abs" style="left:680px;top:600px" width="230" height="90" viewBox="0 0 230 90">
    <path d="M8 20 C0 60 30 90 60 70 C85 50 95 40 115 60 C135 80 150 95 170 80" fill="none" stroke="var(--blue)" stroke-width="3" stroke-linecap="round"/>
  </svg>
  <div class="abs card person-card">
    <div class="avatar" role="img" aria-label="Portrait of staff member"></div>
    <div><b>Lina Berg</b><span>Stockholm</span></div>
  </div>
  <div class="abs card staff-card">
    <div class="label">70+ employee</div>
    <div class="faces">
      <i style="background:#c9a38a"></i><i style="background:#8fa7c4"></i><i style="background:#e08a9a"></i><i class="count">68</i>
    </div>
    <div class="rating"><span style="color:#f5b301">★</span>4.9 <small>(2.1K review)</small></div>
  </div>
  <div class="abs slider-dots"><i></i><i class="on"></i><i></i></div>

  <!-- certificates -->
  <p class="abs cert-line">Our company holds certificates for<br>ISO 9001, ISO 14001, ISO 45001 and "Gnistan".</p>

  <!-- about -->
  <svg class="abs about-img" viewBox="0 0 548 530" role="img" aria-label="Two cleaners in grey uniforms with gloves and a basket of supplies in an office corridor">
    <path d="M0 10 C120 0 300 30 400 10 C500 -10 560 60 540 180 C520 300 530 420 470 480 C410 540 330 520 270 470 C200 410 120 440 0 440Z" fill="#cfe6f7"/>
    <path d="M0 30 C120 20 290 50 380 30 C480 10 520 80 505 190 C490 310 500 420 440 470 C380 520 320 500 260 450 C190 395 110 420 0 430Z" fill="#9aa3ab"/>
  </svg>
  <p class="abs eyebrow">Introduction</p>
  <h2 class="abs about-title">About TRV Clean AB</h2>
  <div class="abs about-rule"></div>
  <p class="abs about-text">Aenean sollicitudin, lorem quis bibendum auctor, nisi elit consequat ipsum, nec sagittis sem nibh id elit. Duis sed odio sit amet nibh vulputate cursus a sit amet mauris. Morbi accumsan ipsum velit. Nam nec tellus a odio tincidunt auctor a ornare odio. Sed non&nbsp; mauris vitae erat consequat auctor eu in elit. Class aptent taciti sociosqu ad litora torquent per conubia nostra, per inceptos himenaeos. Mauris in erat justo...</p>
  <a class="abs btn about-btn" href="#">Find Out More</a>

  <!-- ambitions -->
  <h2 class="abs section-title" style="top:1480px">Our Ambitions</h2>
  <div class="abs title-rule" style="left:569px;top:1542px"></div>
  <div class="abs ambitions">
    <div class="ambition" style="left:164px">
      <div class="circle" style="background:var(--blue)">
        <svg width="54" height="54" viewBox="0 0 54 54" fill="none" stroke="#fff" stroke-width="2.4"><circle cx="27" cy="22" r="15"/><circle cx="27" cy="22" r="9"/><path d="M19 35l-4 14 7-3 4 6 3-15M35 35l4 14-7-3"/></svg>
      </div>
      <p>Quality</p>
    </div>
    <div class="dots3" style="left:296px"><i></i><i style="margin-top:-8px"></i><i></i></div>
    <div class="ambition" style="left:462px">
      <div class="circle" style="background:var(--green)">
        <svg width="56" height="56" viewBox="0 0 56 56" fill="none" stroke="#fff" stroke-width="2.4"><circle cx="26" cy="30" r="17"/><path d="M9 30h34M26 13c-7 8-7 26 0 34M26 13c7 8 7 26 0 34"/><path d="M36 12c4-6 12-6 14-4-1 7-8 10-14 4z" fill="#fff"/></svg>
      </div>
      <p>Environment</p>
    </div>
    <div class="dots3" style="left:596px"><i></i><i style="margin-top:-8px"></i><i></i></div>
    <div class="ambition" style="left:759px">
      <div class="circle" style="background:var(--purple)">
        <svg width="54" height="54" viewBox="0 0 54 54" fill="none" stroke="#fff" stroke-width="2.4"><path d="M17 20a10 10 0 0 1 20 0z"/><circle cx="27" cy="26" r="7"/><path d="M12 50v-6a9 9 0 0 1 9-9h12a9 9 0 0 1 9 9v6z"/><path d="M27 35v15"/></svg>
      </div>
      <p>Labour conditions</p>
    </div>
    <div class="dots3" style="left:874px"><i></i><i style="margin-top:-8px"></i><i></i></div>
    <div class="ambition" style="left:1026px">
      <div class="circle" style="background:var(--yellow)">
        <svg width="54" height="54" viewBox="0 0 54 54" fill="none" stroke="#fff" stroke-width="2.4"><path d="M12 6h22l8 8v18M34 6v8h8M12 6v40h18"/><path d="M18 18h14M18 24h16M18 30h10"/><circle cx="40" cy="38" r="6"/><path d="M36 43l-2 8 6-3 6 3-2-8"/></svg>
      </div>
      <p>Certificates</p>
    </div>
  </div>

  <!-- services -->
  <svg class="abs services-bg" viewBox="0 0 1200 510" preserveAspectRatio="none">
    <path d="M0 110 C180 20 460 0 700 90 C850 150 960 225 1080 205 C1140 195 1180 170 1200 150 V510 H0Z" fill="var(--blue)"/>
    <path d="M0 100 C180 10 460 -10 700 80" fill="none" stroke="#e6f1fa" stroke-width="6"/>
  </svg>
  <div class="abs products-img" role="img" aria-label="Bucket with colourful cleaning bottles, sponges and gloves" style="background:linear-gradient(160deg,#f6c84a,#e84b5b 45%,#4fb6e8)"></div>
  <h2 class="abs section-title services-title">TRV Clean AB Services</h2>
  <div class="abs title-rule" style="left:569px;top:2053px;background:#fff"></div>

  <article class="service" style="left:89px">
    <div class="photo" role="img" aria-label="Cleaner carrying a bucket of supplies in a living room" style="background:linear-gradient(135deg,#d9d3cc,#8fb4d6)"></div>
    <h3>Daily Cleaning</h3>
    <p>Aenean sollicitudin lorem quis bibendum auctorconsequat ipsum nec sagittis sem</p>
  </article>
  <article class="service" style="left:349px">
    <div class="photo" role="img" aria-label="Worker operating a floor cleaning machine in a corridor" style="background:linear-gradient(135deg,#e8e9ea,#9aa1a8)"></div>
    <h3>Floor Care</h3>
    <p>Aenean sollicitudin lorem quis bibendum auctorconsequat ipsum nec sagittis sem</p>
  </article>
  <article class="service" style="left:607px">
    <div class="photo" role="img" aria-label="Cleaner washing a large window with a spray bottle" style="background:linear-gradient(135deg,#cfd9e2,#5c7fa3)"></div>
    <h3>Window Cleaning</h3>
    <p>Aenean sollicitudin lorem quis bibendum auctorconsequat ipsum nec sagittis sem</p>
  </article>
  <article class="service" style="left:866px">
    <div class="photo" role="img" aria-label="Man vacuuming a carpet next to a sofa" style="background:linear-gradient(135deg,#ecebe7,#a9a49b)"></div>
    <h3>Carpet Cleaning</h3>
    <p>Aenean sollicitudin lorem quis bibendum auctorconsequat ipsum nec sagittis sem</p>
  </article>

  <!-- customers -->
  <h2 class="abs customers-title">Our Customers</h2>
  <div class="abs customers-rule"></div>

  <div class="customer" style="left:139px;top:2626px">
    <svg width="60" height="50" viewBox="0 0 60 50" fill="none" stroke="var(--blue)" stroke-width="2"><circle cx="30" cy="11" r="7"/><circle cx="13" cy="19" r="6"/><circle cx="47" cy="19" r="6"/><path d="M18 46V34a12 12 0 0 1 24 0v12zM3 46V36a9 9 0 0 1 14-7M57 46V36a9 9 0 0 0-14-7"/></svg>
    <h4>Public Sector</h4>
    <p>Aenean sollicitudin lorem quis bibendum auctor consequat ipsum nec sagittis</p>
  </div>
  <div class="customer" style="left:442px;top:2626px">
    <svg width="60" height="50" viewBox="0 0 60 50" fill="none" stroke="var(--blue)" stroke-width="2"><path d="M25 2l19 7v14c0 13-9 21-19 25C15 44 6 36 6 23V9z"/><circle cx="25" cy="19" r="6"/><path d="M15 34a10 10 0 0 1 20 0"/><circle cx="42" cy="40" r="8" fill="#fff"/><path d="M38 40l3 3 5-6"/></svg>
    <h4>Private Sector</h4>
    <p>Aenean sollicitudin lorem quis bibendum auctor consequat ipsum nec sagittis</p>
  </div>
  <div class="customer" style="left:139px;top:2794px">
    <svg width="60" height="50" viewBox="0 0 60 50" fill="none" stroke="var(--blue)" stroke-width="2"><circle cx="20" cy="11" r="8"/><path d="M4 46V34a14 14 0 0 1 22-11"/><path d="M28 32l14-12 14 12M32 29v17h20V29"/><path d="M39 46v-8h6v8"/></svg>
    <h4>Home Owner Sector</h4>
    <p>Aenean sollicitudin lorem quis bibendum auctor consequat ipsum nec sagittis</p>
  </div>
  <div class="customer" style="left:442px;top:2794px">
    <svg width="66" height="50" viewBox="0 0 66 50" fill="none" stroke="var(--blue)" stroke-width="2"><path d="M4 46h58M8 46V20h16v26M28 46V8h18v38"/><path d="M12 26h8M12 33h8M32 14h10M32 21h10M32 28h10"/><circle cx="54" cy="12" r="6"/><path d="M46 34a8 8 0 0 1 16 0v12H46z"/></svg>
    <h4>Private Business Sector</h4>
    <p>Aenean sollicitudin lorem quis bibendum auctor consequat ipsum nec sagittis</p>
  </div>

  <svg class="abs worker-art" viewBox="0 0 330 520" role="img" aria-label="Worker in blue overalls holding a paint roller beside a paint bucket, in front of a green leaf shape">
    <path d="M70 100 C150 170 290 220 280 370 C272 470 200 515 130 510 C60 505 15 450 20 380 C25 290 60 210 70 100Z" fill="var(--green)"/>
    <rect x="90" y="10" width="140" height="460" rx="70" fill="#2f63c9" opacity=".55"/>
  </svg>

  <!-- news -->
  <h2 class="abs section-title news-title">Latest News</h2>
  <article class="news" style="left:159px">
    <div class="photo" role="img" aria-label="Two cleaners wiping a glass wall in an office" style="background:linear-gradient(135deg,#b9c3cc,#5f6b77)"></div>
    <div class="body"><time>25-05-2022</time><h3>Some Blog Heading Here</h3><p>Consectetur adipisicing elit, sed do eiusmod tempor dunt ut labore et dolore...</p></div>
  </article>
  <article class="news" style="left:458px">
    <div class="photo" role="img" aria-label="Man mopping a bright living room floor" style="background:linear-gradient(135deg,#eeece8,#b9b2a6)"></div>
    <div class="body"><time>25-05-2022</time><h3>Some Blog Heading Here</h3><p>Consectetur adipisicing elit, sed do eiusmod tempor dunt ut labore et dolore...</p></div>
  </article>
  <article class="news" style="left:756px">
    <div class="photo" role="img" aria-label="Woman wiping a coffee table in a living room" style="background:linear-gradient(135deg,#5b6068,#c7b9a4)"></div>
    <div class="body"><time>25-05-2022</time><h3 style="margin-top:16px">Some Blog Heading Here</h3><p>Consectetur adipisicing elit, sed do eiusmod tempor dunt ut labore et dolore...</p></div>
  </article>

  <!-- footer -->
  <svg class="abs footer-bg" viewBox="0 0 1200 629" preserveAspectRatio="none">
    <rect width="1200" height="629" fill="var(--night)"/>
    <path d="M0 0 H1200 V0 C960 140 680 250 420 238 C240 230 90 150 0 70Z" fill="#fff"/>
    <path d="M0 70 C90 150 240 230 420 238 C680 250 960 140 1200 0" fill="none" stroke="#dcdde0" stroke-width="5"/>
  </svg>

  <section class="abs cta">
    <p class="small">Get a Free Estimate</p>
    <p class="big">Contact for Services</p>
    <a class="go" href="#">Let's Get Started</a>
  </section>

  <footer class="footer">
    <a class="abs logo footer-logo" href="#"><span class="dot"></span>TRV Clean AB</a>
    <div class="abs socials" aria-label="Social media"><i></i><i></i><i></i></div>

    <div class="abs quick">
      <h5>Quick Links</h5>
      <ul><li>Home</li><li>About Us</li><li>Our ambitions</li><li>Our Services</li><li>GDPR Compliance</li><li>News</li><li>Contact Us</li></ul>
    </div>

    <div class="abs contact">
      <h5>Contact Info</h5>
      <div class="row">
        <svg width="14" height="14" viewBox="0 0 12 12"><path d="M2.5 1h2l1 3-1.3 1a7 7 0 0 0 2.8 2.8l1-1.3 3 1v2a1 1 0 0 1-1 1A9.5 9.5 0 0 1 1.5 2a1 1 0 0 1 1-1z" fill="var(--green)"/></svg>
        <div><b>Phone*</b>+46 8 555 010 20</div>
      </div>
      <div class="row">
        <svg width="14" height="14" viewBox="0 0 14 14"><rect x="1" y="3" width="12" height="9" rx="1" fill="var(--green)"/><path d="M1.5 4l5.5 4 5.5-4" fill="none" stroke="#15171f" stroke-width="1.2"/></svg>
        <div><b>Email*</b>info@trvclean.test</div>
      </div>
      <div class="row">
        <svg width="14" height="14" viewBox="0 0 14 14"><path d="M7 1a4.5 4.5 0 0 1 4.5 4.5C11.5 9 7 13 7 13S2.5 9 2.5 5.5A4.5 4.5 0 0 1 7 1z" fill="var(--green)"/><circle cx="7" cy="5.5" r="1.6" fill="#15171f"/></svg>
        <div><b>Location*</b>Somea address line goes here city name</div>
      </div>
    </div>

    <div class="abs newsletter">
      <h5>Our Newsletter</h5>
      <p>Subscribe to our email address to get the latest news.</p>
      <div class="subscribe">
        <svg width="12" height="10" viewBox="0 0 12 10"><rect x=".5" y=".5" width="11" height="9" rx="1" fill="none" stroke="#9aa0a6"/><path d="M1 1l5 4 5-4" fill="none" stroke="#9aa0a6"/></svg>
        <span>Enter Your Email...</span>
        <svg width="14" height="14" viewBox="0 0 14 14"><path d="M1 6.5L13 1 9 13 6.5 8z" fill="var(--green)"/></svg>
      </div>
    </div>

    <div class="abs footer-rule"></div>
    <p class="abs copyright">© Copyright TRV Clean AB 2022 All Rights Reserved</p>
    <p class="abs legal">Terms of use &nbsp;|&nbsp; Privacy Policy</p>
    <a class="abs to-top" href="#" aria-label="Back to top">
      <svg width="14" height="14" viewBox="0 0 14 14"><path d="M7 12V2M3 6l4-4 4 4" fill="none" stroke="#fff" stroke-width="1.6"/></svg>
    </a>
  </footer>

</div>
</body>
</html>
```